New Jar Label for Manuka Honey Company!

Hine Roa Honey, a Manuka Honey company from New Zealand is looking for a fresh & engaging label for our manuka honey jars.

Attached are some examples of label designs that we like, feel free to use the language/copy on these labels for inspiration/content/copy, but feel free to add your own creative spin if you have a great design idea!

LABEL DIMENSIONS: 1654mmx532mm

Label Must Include:
- MGO rating
- Made (or) Product of New Zealand
- Manuka Honey (can add extra text similar to attached examples)

Label Can Include:
- Badges: raw food, non gmo, bpa free, gluten free, halal etc
- anything you feel is appropriate

You can change the color of the logo(s) to Black, White, Silver or Gold.

Can you please include a mockup of your label design(s) on the supplied "Jar Mockup File". You can change the scene of the mockup if you like.

UPDATE:

Have decided on bee logo so please bo longer use the mountain logo for label mockups. Design(s) will need multiple color variations to represent the other MGO ratings, flavor combos and other honey types, other than manuka.

• Provide multiple designs for each honey type
Manuka Design
Spring Honey Design
MGO 100-1000 Design(s)
Wildflower Honey Design
Flavor Combo Honey Design

```html
<!DOCTYPE html>
<html lang="en">
<head>
<meta charset="utf-8">
<title>Hine Roa Honey – Manuka Honey Jar Label</title>
<link href="https://fonts.googleapis.com/css2?family=Montserrat:wght@300;400;700;800&display=swap" rel="stylesheet">
<style>
  :root {
    --page-bg: #ffffff;
    --label-taupe: #86685b;
    --label-taupe-light: #8f7267;
    --label-brown: #54301d;
    --label-brown-deep: #4a2a1c;
    --label-plum: #5e4039;
    --gold: #e8c21e;
    --gold-soft: #d9b42a;
    --white: #ffffff;
    --badge-green: #3cc26a;
    --badge-ring: #2a9a4f;
    --comb-gold: #f2b824;
    --comb-amber: #d6951a;
  }
  * { margin: 0; padding: 0; box-sizing: border-box; }
  html, body {
    width: 1200px;
    height: 1200px;
    overflow: hidden;
    background: var(--page-bg);
    font-family: "Montserrat", sans-serif;
  }
  .canvas {
    position: relative;
    width: 1200px;
    height: 1200px;
  }
  .label {
    position: absolute;
    left: 50px;
    top: 267px;
    width: 1100px;
    height: 667px;
    overflow: hidden;
    background:
      linear-gradient(90deg,
        var(--label-taupe) 0%,
        var(--label-taupe-light) 20%,
        var(--label-brown) 45%,
        var(--label-brown-deep) 65%,
        var(--label-plum) 85%,
        var(--label-plum) 100%);
  }
  .label::after {
    content: "";
    position: absolute;
    inset: 0;
    background: linear-gradient(180deg, rgba(0,0,0,0) 55%, rgba(20,8,4,0.35) 100%);
    pointer-events: none;
  }
  .label p, .label h1 { line-height: 1; white-space: nowrap; position: absolute; left: 74px; z-index: 2; }
  .brand {
    position: absolute;
    left: 74px;
    top: 101px;
    display: flex;
    align-items: center;
    gap: 18px;
    z-index: 2;
  }
  .brand-dot {
    width: 44px;
    height: 44px;
    border-radius: 50%;
    border: 3px solid var(--gold-soft);
  }
  .brand-name {
    font-weight: 400;
    font-size: 30px;
    line-height: 1;
    letter-spacing: 0.16em;
    color: var(--gold-soft);
    text-transform: uppercase;
  }
  .origin {
    top: 228px;
    font-weight: 300;
    font-size: 58px;
    color: var(--white);
  }
  .product {
    top: 324px;
    font-weight: 800;
    font-size: 88px;
    color: var(--white);
  }
  .product .accent { color: var(--gold); }
  .rule {
    position: absolute;
    left: 74px;
    top: 456px;
    width: 534px;
    height: 6px;
    background: var(--gold);
    z-index: 2;
  }
  .rating {
    top: 486px;
    font-weight: 800;
    font-size: 110px;
    color: var(--white);
  }
  .rating .value { color: var(--gold); }
  .badge {
    position: absolute;
    left: 821px;
    top: 136px;
    width: 160px;
    height: 160px;
    border-radius: 50%;
    background: var(--badge-green);
    border: 5px solid var(--badge-ring);
    z-index: 3;
  }
  .honeycomb {
    position: absolute;
    right: 0;
    top: 0;
    width: 160px;
    height: 100%;
    background: linear-gradient(180deg, var(--comb-gold) 0%, var(--comb-amber) 55%, var(--label-plum) 100%);
    z-index: 1;
  }
</style>
</head>
<body>
  <main class="canvas">
    <section class="label">
      <div class="brand">
        <span class="brand-dot"></span>
        <span class="brand-name">Hine Roa Honey</span>
      </div>
      <p class="origin">Product of New Zealand</p>
      <h1 class="product">MANUKA <span class="accent">HONEY</span></h1>
      <div class="rule"></div>
      <p class="rating"><span class="value">829+</span> MGO</p>
      <div class="badge" role="img" aria-label="Non-GMO certification badge"></div>
      <div class="honeycomb" role="img" aria-label="Golden honeycomb with honey bees illustration"></div>
    </section>
  </main>
</body>
</html>
```